Business Card Design for a Design/Build Firm

Kestrel Forge Partners, Inc. is a firm providing construction professional project management and architectural design services to an international clientele. Contemporary. "Green" movement aware. Business card to have back design/logo. Cards will be on high gloss paper

Target Market(s)

Building Developers and Owners

Industry/Entity Type

Construction

Requirements
Nice to have
• We really would like to use the acronym "KFP" as main focal point fo card design. Company will be known as KFP.
Should not have
• No globes or abstract images of buildings.

```html
<!DOCTYPE html>
<html lang="en">
<head>
<meta charset="utf-8">
<title>KFP Business Card</title>
<link href="https://fonts.googleapis.com/css2?family=Anton&family=PT+Sans:wght@400;700&display=swap" rel="stylesheet">
<style>
  :root {
    --bg: #3b3c3e;
    --paper: #f4f4f2;
    --arc-grey: #b3b3b3;
    --ink: #141414;
    --red: #c8161d;
    --red-mid: #a51419;
    --red-deep: #7f0f13;
    --black: #111111;
  }
  * { box-sizing: border-box; margin: 0; padding: 0; }
  html, body { width: 1200px; height: 900px; overflow: hidden; }
  body {
    background: var(--bg);
    font-family: "PT Sans", sans-serif;
    display: flex;
    flex-direction: column;
    align-items: center;
    justify-content: center;
    gap: 56px;
  }
  .card {
    position: relative;
    width: 640px;
    height: 366px;
    background: var(--paper);
    overflow: hidden;
    box-shadow: 0 10px 28px rgba(0,0,0,.45);
  }
  .card-art { position: absolute; inset: 0; width: 100%; height: 100%; }

  /* Front */
  .identity { position: absolute; left: 112px; top: 84px; color: var(--ink); }
  .person-name {
    font-family: "Anton", sans-serif;
    font-size: 30px;
    line-height: 1;
    letter-spacing: .2px;
    font-weight: 400;
  }
  .person-name .surname { color: var(--red); }
  .person-role { font-size: 14px; line-height: 18px; margin-top: 2px; }
  .contact-list { list-style: none; margin-top: 4px; font-size: 15px; line-height: 21px; }
  .contact-list li { display: flex; align-items: center; gap: 8px; }
  .contact-list svg { width: 13px; height: 13px; fill: var(--ink); flex: none; }
  .company-name {
    font-family: "Anton", sans-serif;
    color: var(--red);
    font-size: 15px;
    line-height: 22px;
    letter-spacing: .3px;
  }
  .company-address {
    position: absolute;
    left: 112px;
    top: 244px;
    font-size: 13px;
    line-height: 18px;
    color: var(--ink);
    white-space: nowrap;
  }
  .online {
    position: absolute;
    left: 318px;
    top: 180px;
    list-style: none;
    font-size: 15px;
    line-height: 22px;
    color: var(--ink);
    white-space: nowrap;
  }
  .online li { display: flex; align-items: center; gap: 8px; }
  .online svg { width: 13px; height: 13px; fill: none; stroke: var(--ink); stroke-width: 1.6; flex: none; }
  .online .accent { color: var(--red); }

  .brand { position: absolute; display: flex; align-items: center; gap: 14px; }
  .brand-dot { border-radius: 50%; flex: none; }
  .brand-name { font-family: "Anton", sans-serif; line-height: 1; letter-spacing: 3px; }
  .front .brand { left: 412px; top: 110px; }
  .front .brand-dot { width: 40px; height: 40px; border: 3px solid var(--red); background: var(--paper); }
  .front .brand-name { font-size: 44px; color: var(--ink); }

  /* Back */
  .back .brand { left: 46px; top: 236px; }
  .back .brand-dot { width: 44px; height: 44px; border: 3px solid var(--paper); }
  .back .brand-name { font-size: 54px; color: var(--paper); }
</style>
</head>
<body>

<section class="card front" aria-label="Card front">
  <svg class="card-art" viewBox="0 0 640 366" aria-hidden="true">
    <circle cx="560" cy="640" r="560" fill="var(--arc-grey)"/>
    <circle cx="590" cy="700" r="500" fill="var(--paper)"/>
    <polygon points="24,70 96,52 96,150 24,170" fill="var(--red)"/>
    <rect x="0" y="334" width="640" height="32" fill="var(--black)"/>
  </svg>

  <div class="identity">
    <h1 class="person-name">Marcel<span class="surname">Durand</span></h1>
    <p class="person-role">Managing Director</p>
    <ul class="contact-list">
      <li><svg viewBox="0 0 16 16"><path d="M3 1h4l1 4-2 1a9 9 0 0 0 4 4l1-2 4 1v4c0 1-1 2-2 2A13 13 0 0 1 1 3c0-1 1-2 2-2z"/></svg><span>01632 450118</span></li>
      <li><svg viewBox="0 0 16 16"><path d="M4 1h8v4H4zM1 6h14v7h-3v2H4v-2H1zm4 5v3h6v-3z"/></svg><span>01632 450274</span></li>
      <li><svg viewBox="0 0 16 16"><path d="M4 0h8a1 1 0 0 1 1 1v14a1 1 0 0 1-1 1H4a1 1 0 0 1-1-1V1a1 1 0 0 1 1-1zm1 2v10h6V2zm3 11a1 1 0 1 0 0 2 1 1 0 0 0 0-2z"/></svg><span>+1 55 02 71 36</span></li>
    </ul>
    <p class="company-name">Kestrel Forge Partners, Inc.</p>
  </div>

  <ul class="online">
    <li><svg viewBox="0 0 16 16"><circle cx="8" cy="8" r="6.5"/><path d="M1.5 8h13M8 1.5c3 3 3 10 0 13M8 1.5c-3 3-3 10 0 13"/></svg><span>www.<span class="accent">kestrelforgepartners</span>.co.uk</span></li>
    <li><svg viewBox="0 0 16 16"><rect x="1.5" y="3.5" width="13" height="9"/><path d="M1.5 3.5 8 9l6.5-5.5"/></svg><span>hello@<span class="accent">kestrelforgepartners</span>.co.uk</span></li>
  </ul>

  <p class="company-address">KFP House, 24 Marsh Lane Trading Park, Hartwell Surrey GU9 4RT</p>

  <div class="brand">
    <span class="brand-dot"></span>
    <span class="brand-name">KFP</span>
  </div>
</section>

<section class="card back" aria-label="Card back">
  <svg class="card-art" viewBox="0 0 640 366" aria-hidden="true">
    <circle cx="40" cy="430" r="470" fill="var(--red-deep)"/>
    <circle cx="20" cy="440" r="400" fill="var(--red-mid)"/>
    <circle cx="0" cy="450" r="330" fill="var(--red)"/>
  </svg>
  <div class="brand">
    <span class="brand-dot"></span>
    <span class="brand-name">KFP</span>
  </div>
</section>

</body>
</html>
```